Board to put on a meditation centre - Lantern Hill Haven

I need a board design for a new meditation centre based in Oslo which offers free courses in meditation and self-empowerment. The size of the board is width 374cm x height 104cm.  The name of the meditation centre together with subtitles should be on the board but also some elegant decoration that matches the theme (lantern hill haven/meditation).
Here is the website of the meditation centre to give you a feeling of it: https://lyktebakkenkurs.no/
Good if you can use a blue color close to this one: rgb(37, 180, 193) as well as some brown/golden color (similar to the palette on the website).
On the board it should say:
Lyktebakken senter (in big letters, the rest is subtitles)
Meditasjon & Spirituell visdom
Kurs - Retreat - Dialog
lyktebakkenkurs.no
The design should be very elegant and beautiful and the feeling should be of "An Lantern Hill Haven". A logo is here attached and should be used but I need to get a better quality version of it, will upload that as soon as possible.

```html
<!DOCTYPE html>
<html lang="no">
<head>
<meta charset="utf-8">
<title>Lyktebakken senter – skilt</title>
<link rel="stylesheet" href="https://fonts.googleapis.com/css2?family=Open+Sans:wght@700&family=Ubuntu:wght@400;500&display=swap">
<style>
  :root {
    --backdrop: #8f8f8f;
    --board-top: #2bbfcb;
    --board-bottom: #1a8d98;
    --strip-top: #d6b26c;
    --strip-bottom: #9a7238;
    --art-light: #f6ecd2;
    --art-mid: #7fd3d8;
    --art-dark: #1f8f99;
    --ribbon-gold: #b5843a;
    --accent-gold: #f2d489;
    --text-white: #ffffff;
  }
  * { margin: 0; padding: 0; box-sizing: border-box; }
  html, body {
    width: 1200px; height: 462px; overflow: hidden;
    background: var(--backdrop);
  }
  .board {
    position: absolute; left: 79px; top: 86px;
    width: 1042px; height: 290px;
    background: linear-gradient(to bottom, var(--board-top), var(--board-bottom));
    overflow: hidden;
    font-family: "Ubuntu", sans-serif;
    color: var(--text-white);
  }
  .accent-strip {
    position: absolute; left: 79px; top: 0;
    width: 150px; height: 290px;
    background: linear-gradient(to bottom, var(--strip-top), var(--strip-bottom));
  }
  .meditation-artwork {
    position: absolute; left: 8px; top: 14px;
    width: 304px; height: 268px;
    border-radius: 40% 40% 12px 12px;
    background: radial-gradient(ellipse at 50% 55%, var(--art-light) 0%, #d9efe6 28%, var(--art-mid) 55%, var(--art-dark) 100%);
  }
  .centre-name {
    position: absolute; left: 316px; width: 530px; top: 62px;
    text-align: center;
    font-family: "Open Sans", sans-serif; font-weight: 700;
    font-size: 46px; line-height: 1; letter-spacing: 0.5px;
    white-space: nowrap;
  }
  .tagline {
    position: absolute; left: 316px; width: 530px; top: 127px;
    text-align: center; font-size: 29px; line-height: 34px; font-weight: 400;
  }
  .offer-ribbon {
    position: absolute; left: 381px; top: 180px;
    width: 347px; height: 36px;
  }
  .offer-ribbon svg { position: absolute; inset: 0; }
  .offer-ribbon span {
    position: relative; display: block; text-align: center;
    font-size: 26px; line-height: 36px; font-weight: 400;
  }
  .web-address {
    position: absolute; left: 316px; width: 530px; top: 232px;
    text-align: center; font-size: 17px; letter-spacing: 1.6px;
  }
  .brand-mark {
    position: absolute; left: 855px; top: 92px; width: 160px;
    display: flex; flex-direction: column; align-items: center; gap: 12px;
  }
  .brand-mark .dot {
    width: 70px; height: 70px; border-radius: 50%;
    background: var(--accent-gold);
  }
  .brand-mark .brand-name {
    font-size: 19px; font-weight: 500; color: var(--accent-gold);
    white-space: nowrap;
  }
</style>
</head>
<body>
  <main class="board">
    <div class="accent-strip"></div>
    <div class="meditation-artwork" role="img" aria-label="Paper-cut style illustration of a white silhouette seated in lotus meditation, surrounded by tropical leaves and soft golden flowers"></div>

    <h1 class="centre-name">LYKTEBAKKEN SENTER</h1>
    <p class="tagline">Meditasjon &amp; Spirituell visdom</p>

    <div class="offer-ribbon">
      <svg viewBox="0 0 347 36" width="347" height="36" preserveAspectRatio="none" aria-hidden="true">
        <polygon points="0,0 347,0 337,18 347,36 0,36 10,18" fill="var(--ribbon-gold)"/>
      </svg>
      <span>Kurs - Retreat - Dialog</span>
    </div>

    <p class="web-address">www.lyktebakkenkurs.no</p>

    <div class="brand-mark">
      <div class="dot"></div>
      <div class="brand-name">Lyktebakken senter</div>
    </div>
  </main>
</body>
</html>
```